Updated brief for New ecommerce site needs a stunning business card that links to web site.

Updated business card brief. Please refer to the new files uploaded today (the last two) which show the background colour/style that we will be using in our web template for on-line trading, the grey marble concrete look.

Please see if you can use the grey marble background in the business card design in a way so it relates to our web template. It also needs to be transferable to banner ad, chatterbox ad etc.
vantor hub is a NEW eCommerce website which is commencing selling via bidnook & swapcrate, used & damaged mobile phones & accessories, evolving into a full eCommerce store.

We like strong clean lines, use of a circle, in essence this will become our logo as well. Colours strong orange/Black/White The orange stronger than in PixelHerd #8164937 & grey marble as per file attached #274615

We love the use of a circle!! As we are evolving & moving forward this is what the circle represents to us……. ongoing change.

Front side with a circle with vantor hub in a modern font in the middle, vantor is in a strong orange and group is in black or white. On the reverse side, use layout as per Snapwell design from plonk.com. for icon details (not the boarder at top/botto).

This design is to meet www.plonk.com luxe cards specifications
Thank you we look forward to last minute inspiration.

Project Deadline Extended Reason: Hi We need to extend our deadline to ensure we don't rush the design. We are close to getting what we want, however due to work commitments here we need a couple more days to work this through to ensure the concept ties in with our other marketing.Thank you for understanding and your patience.vantorhub Added Tuesday, March 3, 2015

Target Market(s)

Suppliers & business networking

Industry/Entity Type

Business

Contact Information for Business Card

Liam Presk
Director
mob +61 4987 6543
Locked Bag WXYZ 5678 QRS
liam@vantorhub.example.au
www.vantorhub.example.au

Requirements
Must have
• Design to meet www.plonk.com luxe business card specifications
• Colours - orange needs to be bold and strong & /black/white
• Circle with vantor hub in the middle
Nice to have
• Grey marble background incorporated into design in someway so it links with our web page.

```html
<!DOCTYPE html>
<html lang="en">
<head>
<meta charset="utf-8">
<title>vantorhub business card</title>
<link rel="stylesheet" href="https://fonts.googleapis.com/css2?family=Iceland&display=swap">
<style>
  :root {
    --backdrop: #c8c8c8;
    --orange: #ec6a2e;
    --black: #0b0b0b;
    --white: #ffffff;
    --type: "Iceland", "Arial Narrow", sans-serif;
  }
  * { margin: 0; padding: 0; box-sizing: border-box; }
  html, body {
    width: 1200px;
    height: 799px;
    overflow: hidden;
    background: var(--backdrop);
    font-family: var(--type);
  }
  .canvas {
    position: relative;
    width: 1200px;
    height: 799px;
  }
  .card {
    position: absolute;
    top: 145px;
    width: 310px;
    height: 505px;
    box-shadow: 0 4px 14px rgba(0,0,0,0.18);
  }
  /* contact side */
  .card-back {
    left: 250px;
    background: var(--white);
  }
  .contact-panel {
    position: absolute;
    top: 14px;
    left: 14px;
    right: 14px;
    height: 355px;
    background: var(--black);
    padding: 80px 16px 0 30px;
    overflow: hidden;
  }
  .person-name {
    color: var(--orange);
    font-size: 40px;
    font-weight: 400;
    line-height: 1;
    letter-spacing: 1px;
    white-space: nowrap;
  }
  .person-role {
    color: var(--white);
    font-size: 22px;
    letter-spacing: 2px;
    margin-top: 4px;
  }
  .contact-list {
    list-style: none;
    margin-top: 30px;
  }
  .contact-item {
    display: flex;
    align-items: center;
    gap: 10px;
    color: var(--white);
    font-size: 14px;
    letter-spacing: 0.8px;
    height: 30px;
    white-space: nowrap;
  }
  .contact-icon {
    width: 14px;
    height: 14px;
    flex: none;
    fill: none;
    stroke: var(--orange);
    stroke-width: 1.8;
  }
  .back-wordmark {
    position: absolute;
    left: 0;
    right: 0;
    bottom: 48px;
    text-align: center;
    color: var(--orange);
    font-size: 50px;
    letter-spacing: 1px;
    line-height: 1;
  }
  /* logo side */
  .card-front {
    left: 640px;
    background: var(--orange);
  }
  .logo-circle {
    position: absolute;
    top: 60px;
    left: 30px;
    width: 250px;
    height: 250px;
    border-radius: 50%;
    background: var(--white);
    display: flex;
    align-items: center;
    justify-content: center;
  }
  .front-wordmark {
    color: var(--orange);
    font-size: 44px;
    letter-spacing: 1px;
    line-height: 1;
    white-space: nowrap;
  }
</style>
</head>
<body>
<main class="canvas">
  <section class="card card-back" aria-label="Contact side">
    <div class="contact-panel">
      <h1 class="person-name">Liam Presk</h1>
      <p class="person-role">Director</p>
      <ul class="contact-list">
        <li class="contact-item">
          <svg class="contact-icon" viewBox="0 0 14 14" aria-hidden="true"><rect x="3.5" y="1" width="7" height="12" rx="1.2"/><line x1="6" y1="11" x2="8" y2="11"/></svg>
          +61 4987 6543
        </li>
        <li class="contact-item">
          <svg class="contact-icon" viewBox="0 0 14 14" aria-hidden="true"><path d="M7 13 C3 8.5 2.5 6.8 2.5 5.3 A4.5 4.5 0 0 1 11.5 5.3 C11.5 6.8 11 8.5 7 13 Z"/><circle cx="7" cy="5.3" r="1.6"/></svg>
          Locked Bag WXYZ 5678 QRS
        </li>
        <li class="contact-item">
          <svg class="contact-icon" viewBox="0 0 14 14" aria-hidden="true"><rect x="1" y="3" width="12" height="8.5"/><path d="M1 3 L7 8 L13 3"/></svg>
          liam@vantorhub.example.au
        </li>
        <li class="contact-item">
          <svg class="contact-icon" viewBox="0 0 14 14" aria-hidden="true"><circle cx="7" cy="7" r="5.8"/><ellipse cx="7" cy="7" rx="2.5" ry="5.8"/><line x1="1.2" y1="7" x2="12.8" y2="7"/></svg>
          www.vantorhub.example.au
        </li>
      </ul>
    </div>
    <p class="back-wordmark">vantorhub</p>
  </section>

  <section class="card card-front" aria-label="Logo side">
    <div class="logo-circle">
      <p class="front-wordmark">vantorhub</p>
    </div>
  </section>
</main>
</body>
</html>
```